Graphic Design Vendora Book Description

There is a book on Vendora that is my competitor that has a large graphic design as part of the description for the book and I want a similar thing for my book to make it stand out more.

My competitors book is here: https://www.vendora-shop.example/Tidal-Lore-Starters-Grasping-Overview/dp/K31RTWP704/

My book is here: https://www.vendora-shop.example/Tidal-Lore-Groundwork-Workings-Interlacing/dp/K7Q2FXH58C/

You can see the kind of thing I am looking for on the book listing but I have attached an image below.

Thanks

Colin

```html
<!DOCTYPE html>
<html lang="en">
<head>
<meta charset="UTF-8">
<title>Quantum Physics – Book Cover</title>
<link href="https://fonts.googleapis.com/css2?family=Montserrat:wght@600;700;800&display=swap" rel="stylesheet">
<style>
  :root {
    --page-bg: #e6e8ec;
    --cover-top: #0d1322;
    --cover-bottom: #070a12;
    --ink-white: #f4f6fa;
    --ink-soft: #dfe5ef;
    --glow-blue: #2f8dff;
    --glow-core: #6fc0ff;
    --glow-deep: #0b2a66;
  }
  * { margin: 0; padding: 0; box-sizing: border-box; }
  html, body {
    width: 1200px;
    height: 1200px;
    overflow: hidden;
    background: var(--page-bg);
  }
  .canvas {
    width: 1200px;
    height: 1200px;
    display: flex;
    align-items: center;
    justify-content: center;
  }
  .book-cover {
    position: relative;
    width: 760px;
    height: 1120px;
    background: linear-gradient(180deg, var(--cover-top) 0%, var(--cover-bottom) 100%);
    font-family: "Montserrat", sans-serif;
    color: var(--ink-white);
    text-align: center;
    overflow: hidden;
  }
  .cover-title {
    position: absolute;
    top: 90px;
    left: 0;
    right: 0;
    font-weight: 800;
    font-size: 84px;
    line-height: 1.12;
    letter-spacing: 3px;
    text-transform: uppercase;
  }
  .cover-art {
    position: absolute;
    top: 330px;
    left: 50%;
    width: 460px;
    height: 460px;
    margin-left: -230px;
    border-radius: 50%;
    background: radial-gradient(circle at 50% 50%,
      var(--glow-core) 0%,
      var(--glow-blue) 18%,
      var(--glow-deep) 48%,
      rgba(11, 42, 102, 0.25) 68%,
      rgba(11, 42, 102, 0) 72%);
  }
  .cover-subtitle {
    position: absolute;
    top: 850px;
    left: 80px;
    right: 80px;
    font-weight: 700;
    font-size: 26px;
    line-height: 1.3;
    letter-spacing: 0.5px;
    text-transform: uppercase;
    color: var(--ink-soft);
  }
  .cover-author {
    position: absolute;
    bottom: 50px;
    left: 0;
    right: 0;
    font-weight: 800;
    font-size: 58px;
    letter-spacing: 3px;
    text-transform: uppercase;
  }
</style>
</head>
<body>
  <main class="canvas">
    <section class="book-cover">
      <h1 class="cover-title">Quantum<br>Physics</h1>
      <div class="cover-art" role="img" aria-label="Glowing blue atom illustration with a bright nucleus and electrons on crossing orbital rings"></div>
      <p class="cover-subtitle">A Beginners Guide to Quantum Mechanics, String Theory, Field Theory, and Quantum Computing</p>
      <p class="cover-author">Elias Thorne</p>
    </section>
  </main>
</body>
</html>
```